Prom Night 2011 theme

I am looking for a theme to best represent a high school "prom night". Design will be printed on slightly smaller than business card size paper. This is a clean sheet design, nothing is out of bounds so use you imagination. Target audience is high school age students. Design should have text "Prom Night 2011" incorporated into it. Colors are limitless.

```html
<!DOCTYPE html>
<html lang="en">
<head>
<meta charset="utf-8">
<title>Prom Night 2011 – Card Set</title>
<link rel="stylesheet" href="https://fonts.googleapis.com/css2?family=Allura&family=Yellowtail&family=Arimo:wght@700&display=swap">
<style>
  :root {
    --page: #ffffff;
    --red-light: #d62a27;
    --red-mid: #b51d1b;
    --red-dark: #7e0f0e;
    --band-light: #ffffff;
    --band-shade: #d9d9d9;
    --ink: #1a1a1a;
    --white: #ffffff;
    --emblem-dark: #8f1412;
  }
  * { box-sizing: border-box; margin: 0; padding: 0; }
  html, body {
    width: 1200px; height: 900px; overflow: hidden;
    background: var(--page);
  }
  .canvas {
    position: relative; width: 1200px; height: 900px;
    display: flex; align-items: center; justify-content: center; gap: 60px;
  }
  .card {
    position: relative; width: 520px; height: 356px;
    border-radius: 16px; overflow: hidden;
    background: radial-gradient(ellipse at 50% 45%, var(--red-light) 0%, var(--red-mid) 55%, var(--red-dark) 100%);
  }

  /* Front */
  .front-band {
    position: absolute; left: 0; right: 0; top: 136px; height: 62px;
    background: linear-gradient(180deg, var(--band-light) 0%, #f2f2f2 55%, var(--band-shade) 100%);
  }
  .front-emblem {
    position: absolute; left: 40px; top: 110px; width: 114px; height: 114px;
    border-radius: 50%;
    background: radial-gradient(circle at 45% 45%, var(--red-light) 0%, var(--emblem-dark) 100%);
    border: 6px solid var(--white);
  }
  .front-title {
    position: absolute; right: 28px; top: 140px;
    font-family: "Allura", cursive; font-size: 40px; color: var(--ink);
    white-space: nowrap;
  }
  .front-title .year {
    font-family: "Yellowtail", cursive; font-size: 40px;
  }

  /* Back */
  .back-title {
    position: absolute; left: 14px; top: 6px;
    font-family: "Allura", cursive; font-size: 28px; color: var(--white);
    white-space: nowrap;
  }
  .back-title .year { font-family: "Yellowtail", cursive; }
  .back-emblem {
    position: absolute; left: 50px; top: 70px; width: 200px; height: 200px;
    border-radius: 50%;
    background: radial-gradient(circle at 50% 45%, rgba(150,20,18,0.55) 0%, rgba(150,20,18,0.25) 70%, rgba(150,20,18,0) 100%);
  }
  .holder-name {
    position: absolute; left: 244px; top: 82px;
    font-family: "Yellowtail", cursive; font-size: 92px; line-height: 1;
    color: var(--white);
  }
  .holder-contact {
    position: absolute; left: 338px; top: 168px;
    font-family: "Arimo", sans-serif; font-weight: 700; font-size: 14px;
    line-height: 17px; color: var(--white); list-style: none;
  }
</style>
</head>
<body>
<main class="canvas">
  <section class="card card-front">
    <div class="front-band"></div>
    <div class="front-emblem" role="img" aria-label="Illustration of a prom couple seated on a crescent moon"></div>
    <h1 class="front-title">Prom Night <span class="year">2011</span></h1>
  </section>

  <section class="card card-back">
    <p class="back-title">Prom Night <span class="year">2011</span></p>
    <div class="back-emblem" role="img" aria-label="Faint illustration of a prom couple on a crescent moon"></div>
    <h2 class="holder-name">Delia</h2>
    <ul class="holder-contact">
      <li>Harbor Court 41820</li>
      <li>Maple Ridge</li>
      <li>delia@mailbox.test</li>
      <li>(054)8190347</li>
    </ul>
  </section>
</main>
</body>
</html>
```